Varn Medical needs bold attention catching website for healthcare professionals(target)

I need a hero page as well as a products and about page for a website of mine. I specialize in orthopedic instruments . Specifically bone drills and saws. This whole company was founded to bring superb quality highly discounted medical instruments. Specifically bone drills, bone saws, k-wires and pins. Two main points should be cost savings and superior quality.

Target Market(s)

healthcare professionals Surgeons and hospital material managers

Number of Pages Required

3 page

Font styles to use
Serif

Colors

Designer to choose colors to be used in the design.

Requirements
Must have
• colors should match logo design

```html
<!DOCTYPE html>
<html lang="en">
<head>
<meta charset="utf-8">
<title>Varn Medical</title>
<link rel="stylesheet" href="https://fonts.googleapis.com/css2?family=Roboto+Slab:wght@300;400;500;600;700;800;900&family=Source+Serif+4:wght@400;600;700&display=swap">
<style>
:root{
  --red:#e8340c;
  --red-deep:#c81f05;
  --red-light:#ff5a1f;
  --ink:#1a1a1a;
  --black:#0b0b0b;
  --line:#e3e3e3;
  --white:#fff;
  --sky:#5fa9dc;
  --sky-light:#cfe6f6;
  --violet:#b77fd6;
  --display:"Roboto Slab",serif;
  --text:"Source Serif 4",serif;
}
*{box-sizing:border-box;margin:0;padding:0}
html,body{width:1200px;height:2757px;overflow:hidden}
body{position:relative;background:var(--white);font-family:var(--text);color:var(--ink)}
.abs{position:absolute}
/* header */
.brand{left:290px;top:36px;display:flex;align-items:center;gap:10px;font-family:var(--display);font-size:32px;font-weight:600;color:var(--red)}
.brand-dot{width:14px;height:14px;border-radius:50%;background:var(--red)}
.help{right:258px;top:36px;text-align:right;font-family:var(--display)}
.help-label{font-size:13px;font-weight:800;letter-spacing:.3px}
.help-phone{display:flex;align-items:center;justify-content:flex-end;gap:6px;font-size:25px;font-weight:800;color:var(--red);line-height:1.1}
.help-hours{font-family:var(--text);font-size:8px;margin-top:3px}
.nav{left:0;top:120px;width:1200px;height:48px;background:var(--black)}
.nav ul{list-style:none;display:flex;gap:27px;position:absolute;left:257px;top:18px}
.nav li{font-family:var(--display);font-size:10px;font-weight:500;color:#ddd;letter-spacing:.4px;position:relative}
.nav li.active::after{content:"";position:absolute;left:0;right:0;top:21px;height:3px;background:var(--red)}
.nav li.active::before{content:"";position:absolute;left:50%;top:24px;margin-left:-6px;border:6px solid transparent;border-top-color:var(--red)}
/* bands */
.band{left:0;width:1200px}
.band-sky{top:195px;height:348px;background:linear-gradient(100deg,#3b8fd0 0%,var(--sky) 35%,var(--sky-light) 75%,#eef6fb 100%)}
.band-room{top:1174px;height:361px;background:linear-gradient(100deg,#c88ed8 0%,var(--violet) 30%,#d9b7e6 65%,#ece2ef 100%)}
.band-tech{top:1808px;height:349px;background:linear-gradient(100deg,#2c4e7a 0%,#12355a 45%,#0a2036 100%)}
.promo{width:333px;height:282px;padding:26px 18px 0;color:var(--white)}
.promo-red{background:linear-gradient(150deg,var(--red-light),var(--red-deep))}
.promo-dark{background:rgba(0,0,0,.9)}
.promo-title{font-family:var(--display);font-size:41px;font-weight:900;line-height:46px;letter-spacing:-.5px;text-transform:uppercase}
.promo-sub{font-family:var(--display);font-size:28px;font-weight:300;line-height:34px;text-transform:uppercase}
.promo p{font-size:9px;line-height:15px;width:230px;margin-top:16px;opacity:.85}
.promo .go{position:absolute;right:18px;bottom:22px}
.go{width:46px;height:46px;border:1.5px solid rgba(255,255,255,.85);display:flex;align-items:center;justify-content:center}
/* tiles */
.tile{width:333px;height:177px;color:var(--white);overflow:hidden}
.tile-red{background:linear-gradient(120deg,var(--red) 0%,#b0280c 60%,#4a1a10 100%)}
.tile-dark{background:linear-gradient(120deg,#121212 0%,#2b2b2b 55%,#1a1a1a 100%)}
.tile h3{position:absolute;left:16px;top:78px;font-family:var(--display);font-size:30px;font-weight:900;letter-spacing:.3px}
.tile p{position:absolute;left:16px;top:120px;width:190px;font-size:8.5px;line-height:15px;opacity:.75}
.tile .sq{position:absolute;right:26px;top:117px;width:38px;height:38px;display:flex;align-items:center;justify-content:center}
.sq-dark{background:#1a1a1a}
.sq-red{background:var(--red)}
/* headings */
.heading{font-family:var(--display);font-size:30px;line-height:34px;color:var(--red);text-transform:uppercase}
.heading b{font-weight:900;display:block}
.heading span{font-weight:300}
.body-text{font-size:9.5px;line-height:15.4px;color:#333}
.btn{width:97px;height:39px;background:var(--black);color:#eee;font-family:var(--display);font-size:10px;display:flex;align-items:center;justify-content:center;letter-spacing:.4px}
/* products */
.products-title{left:258px;top:1560px;font-family:var(--display);font-size:32px;font-weight:300;color:var(--black)}
.products-title b{font-weight:900}
.plist{top:1612px;width:216px;list-style:none}
.plist li{height:33px;border-bottom:1px solid var(--line);display:flex;align-items:center;gap:10px;padding-left:10px;font-family:var(--display);font-size:10px;font-weight:700;color:var(--red);text-transform:uppercase}
.plist li.on{background:var(--red);color:var(--white)}
/* footer */
.footer{left:0;top:2475px;width:1200px;height:282px;background:#0e0e0e}
.footer-base{left:0;top:2715px;width:1200px;height:42px;background:#050505}
.footer-title{left:258px;top:2505px;font-family:var(--display);font-size:30px;font-weight:900;color:var(--white)}
.contact-list{left:258px;top:2565px;list-style:none}
.contact-list li{font-size:9px;color:#888;margin-bottom:12px}
.contact-list em{font-style:normal;color:var(--red);text-transform:uppercase;margin-right:2px}
.copyright{left:258px;top:2732px;font-size:7px;color:#444}
</style>
</head>
<body>

<div class="abs brand"><span>Varn Medical</span><span class="brand-dot"></span></div>
<div class="abs help">
  <div class="help-label">NEED HELP?</div>
  <div class="help-phone">
    <svg width="14" height="22" viewBox="0 0 14 22"><rect x="1" y="1" width="12" height="20" rx="2" fill="none" stroke="#888" stroke-width="2"/><circle cx="7" cy="17" r="1.3" fill="#888"/></svg>
    800-555-0142
  </div>
  <div class="help-hours"><b>Hours:</b> 6am-4pm PST M-Th; &nbsp;6am-3pm PST Fri</div>
</div>
<nav class="abs nav">
  <ul>
    <li class="active">HOME</li><li>ABOUT US</li><li>PRODUCTS &amp; SERVICES</li><li>PROJECT GALLERY</li><li>CONTACTS</li>
  </ul>
</nav>

<div class="abs band band-sky" role="img" aria-label="Photo of a doctor's hand holding a stethoscope over a blue globe with a heartbeat line"></div>
<div class="abs promo promo-red" style="left:260px;top:226px">
  <div class="promo-title">A complete<br>line of</div>
  <div class="promo-sub">products is<br>available</div>
  <p>Bone drills, saws, k-wires and pins built to surgical standards and priced well below usual hospital lists.</p>
  <div class="go"><svg width="12" height="18" viewBox="0 0 12 18"><path d="M2 2l7 7-7 7" fill="none" stroke="#fff" stroke-width="2"/></svg></div>
</div>

<div class="abs tile tile-red" style="left:258px;top:565px" role="img" aria-label="Photo of an orthopedic bone drill">
  <h3>BONE DRILLS</h3><p>Cordless and cannulated drills with steady torque for theatre work.</p>
  <div class="sq sq-dark"><svg width="9" height="14" viewBox="0 0 9 14"><path d="M1.5 1.5l5.5 5.5-5.5 5.5" fill="none" stroke="#fff" stroke-width="1.8"/></svg></div>
</div>
<div class="abs tile tile-dark" style="left:609px;top:565px" role="img" aria-label="Photo of an oscillating bone saw">
  <h3>BONE SAWS</h3><p>Sagittal and oscillating saws with blades cut for clean bone work.</p>
  <div class="sq sq-red"><svg width="9" height="14" viewBox="0 0 9 14"><path d="M1.5 1.5l5.5 5.5-5.5 5.5" fill="none" stroke="#fff" stroke-width="1.8"/></svg></div>
</div>
<div class="abs tile tile-dark" style="left:258px;top:759px" role="img" aria-label="Photo of a set of k-wires">
  <h3>K-WIRES</h3><p>Smooth and threaded wires in every common gauge and length.</p>
  <div class="sq sq-red"><svg width="9" height="14" viewBox="0 0 9 14"><path d="M1.5 1.5l5.5 5.5-5.5 5.5" fill="none" stroke="#fff" stroke-width="1.8"/></svg></div>
</div>
<div class="abs tile tile-dark" style="left:609px;top:759px" role="img" aria-label="Photo of surgical steel pins">
  <h3>PINS</h3><p>Steinmann and Schanz pins with trocar and diamond tip styles.</p>
  <div class="sq sq-red"><svg width="9" height="14" viewBox="0 0 9 14"><path d="M1.5 1.5l5.5 5.5-5.5 5.5" fill="none" stroke="#fff" stroke-width="1.8"/></svg></div>
</div>

<h2 class="abs heading" style="left:258px;top:960px"><b>We'll handle any</b><span>intricate custom design</span></h2>
<p class="abs body-text" style="left:258px;top:1033px;width:320px">Every instrument we supply is inspected against strict surgical standards before it ships. Our drills and saws deliver the torque, balance and reliability surgeons expect, while direct sourcing keeps prices well below typical hospital contracts. Material managers gain predictable costs, fast delivery and responsive support. From single replacements to full theatre sets, we match each order to your specifications and stand behind every unit with clear warranties.</p>
<p class="abs body-text" style="left:609px;top:1033px;width:320px">Need a special length, gauge or attachment? Our team works with your surgeons to supply instruments that fit existing systems. Quality stays superior, and the savings stay real.</p>
<div class="abs btn" style="left:609px;top:1127px">READ MORE</div>

<div class="abs band band-room" role="img" aria-label="Photo of a hospital room with a bed and a medical cart"></div>
<div class="abs promo promo-red" style="left:258px;top:1225px">
  <div class="promo-title">We serve<br>to meet</div>
  <div class="promo-sub">your fabrication<br>needs</div>
  <p>Fast quotes, short lead times and instruments built to the exact needs of your operating team.</p>
  <div class="go"><svg width="12" height="18" viewBox="0 0 12 18"><path d="M2 2l7 7-7 7" fill="none" stroke="#fff" stroke-width="2"/></svg></div>
</div>

<h2 class="abs products-title"><b>OUR</b> PRODUCTS</h2>
<ul class="abs plist" style="left:258px">
  <li><svg width="7" height="10" viewBox="0 0 7 10"><path d="M1 1l4 4-4 4" fill="none" stroke="currentColor" stroke-width="1.6"/></svg>Cordless bone drill</li>
  <li class="on"><svg width="7" height="10" viewBox="0 0 7 10"><path d="M1 1l4 4-4 4" fill="none" stroke="currentColor" stroke-width="1.6"/></svg>Cannulated drill</li>
  <li><svg width="7" height="10" viewBox="0 0 7 10"><path d="M1 1l4 4-4 4" fill="none" stroke="currentColor" stroke-width="1.6"/></svg>Mini drill set</li>
  <li><svg width="7" height="10" viewBox="0 0 7 10"><path d="M1 1l4 4-4 4" fill="none" stroke="currentColor" stroke-width="1.6"/></svg>Battery packs</li>
  <li><svg width="7" height="10" viewBox="0 0 7 10"><path d="M1 1l4 4-4 4" fill="none" stroke="currentColor" stroke-width="1.6"/></svg>Drill chucks</li>
  <li><svg width="7" height="10" viewBox="0 0 7 10"><path d="M1 1l4 4-4 4" fill="none" stroke="currentColor" stroke-width="1.6"/></svg>Twist drill bits</li>
</ul>
<ul class="abs plist" style="left:494px">
  <li><svg width="7" height="10" viewBox="0 0 7 10"><path d="M1 1l4 4-4 4" fill="none" stroke="currentColor" stroke-width="1.6"/></svg>Sagittal saw</li>
  <li><svg width="7" height="10" viewBox="0 0 7 10"><path d="M1 1l4 4-4 4" fill="none" stroke="currentColor" stroke-width="1.6"/></svg>Oscillating saw</li>
  <li><svg width="7" height="10" viewBox="0 0 7 10"><path d="M1 1l4 4-4 4" fill="none" stroke="currentColor" stroke-width="1.6"/></svg>Reciprocating saw</li>
  <li><svg width="7" height="10" viewBox="0 0 7 10"><path d="M1 1l4 4-4 4" fill="none" stroke="currentColor" stroke-width="1.6"/></svg>Sternum saw</li>
  <li><svg width="7" height="10" viewBox="0 0 7 10"><path d="M1 1l4 4-4 4" fill="none" stroke="currentColor" stroke-width="1.6"/></svg>Saw blades</li>
  <li><svg width="7" height="10" viewBox="0 0 7 10"><path d="M1 1l4 4-4 4" fill="none" stroke="currentColor" stroke-width="1.6"/></svg>Saw hand pieces</li>
</ul>
<ul class="abs plist" style="left:729px">
  <li><svg width="7" height="10" viewBox="0 0 7 10"><path d="M1 1l4 4-4 4" fill="none" stroke="currentColor" stroke-width="1.6"/></svg>Smooth k-wires</li>
  <li><svg width="7" height="10" viewBox="0 0 7 10"><path d="M1 1l4 4-4 4" fill="none" stroke="currentColor" stroke-width="1.6"/></svg>Threaded k-wires</li>
  <li><svg width="7" height="10" viewBox="0 0 7 10"><path d="M1 1l4 4-4 4" fill="none" stroke="currentColor" stroke-width="1.6"/></svg>Steinmann pins</li>
  <li><svg width="7" height="10" viewBox="0 0 7 10"><path d="M1 1l4 4-4 4" fill="none" stroke="currentColor" stroke-width="1.6"/></svg>Schanz pins</li>
  <li><svg width="7" height="10" viewBox="0 0 7 10"><path d="M1 1l4 4-4 4" fill="none" stroke="currentColor" stroke-width="1.6"/></svg>Wire drivers</li>
  <li><svg width="7" height="10" viewBox="0 0 7 10"><path d="M1 1l4 4-4 4" fill="none" stroke="currentColor" stroke-width="1.6"/></svg>Pin cutters</li>
</ul>

<div class="abs band band-tech" role="img" aria-label="Photo of a hand touching a screen of glowing hexagon medical icons"></div>
<div class="abs promo promo-dark" style="left:258px;top:1847px;height:286px">
  <div class="promo-title">We meet<br>a wide</div>
  <div class="promo-sub">range of fabri-<br>cation require-<br>ments</div>
  <p style="margin-top:10px">From trauma cases to elective joint work, one reliable supplier.</p>
  <div class="go"><svg width="12" height="18" viewBox="0 0 12 18"><path d="M2 2l7 7-7 7" fill="none" stroke="#fff" stroke-width="2"/></svg></div>
</div>

<h2 class="abs heading" style="left:258px;top:2180px"><b>Offering the best level</b><span>of excellence in steel fabrication</span></h2>
<div class="abs" style="left:258px;top:2263px;width:333px;height:182px;background:linear-gradient(120deg,#f4f6f8 0%,#e9edf0 50%,#f7d2b8 100%)" role="img" aria-label="Photo of two surgical steel pins on a light background"></div>
<p class="abs body-text" style="left:609px;top:2257px;width:320px">Our stainless steel is machined, polished and passivated to resist corrosion through repeated sterilisation cycles. Each drill, saw blade, k-wire and pin is traceable by lot and tested for tolerance and sharpness. Surgeons get dependable performance in every case, and hospitals get that quality at a fraction of the usual cost, backed by fast replacement and honest, direct pricing.</p>
<div class="abs btn" style="left:609px;top:2388px">READ MORE</div>

<div class="abs footer"></div>
<div class="abs footer-base"></div>
<h2 class="abs footer-title">CONTACTS</h2>
<ul class="abs contact-list">
  <li><em>Free phone:</em> 800-555-0142</li>
  <li><em>Address:</em> 212 Harbor Lane Glasgow G12 4QX</li>
  <li><em>Hours:</em> 6am-4pm PST M-Th; &nbsp;6am-3pm PST Fri</li>
  <li><em>E-mail:</em> <span style="color:var(--red)">info@varnmedical.example</span></li>
</ul>
<div class="abs" style="left:609px;top:2508px;width:333px;height:182px;background:linear-gradient(135deg,#2a2a2a,#1b1b1b)" role="img" aria-label="Map showing the office location"></div>
<svg class="abs" style="left:762px;top:2568px" width="34" height="46" viewBox="0 0 34 46"><path d="M17 2C9 2 3 8 3 16c0 11 14 27 14 27s14-16 14-27C31 8 25 2 17 2z" fill="var(--red)"/><circle cx="17" cy="16" r="5" fill="#8c1a05"/></svg>
<div class="abs copyright">Varn Medical &copy; 2024 &nbsp;Privacy Policy</div>

</body>
</html>
```